Business Card Design Project

Looking to update our business cards. We have a logo with our slogan. We are an IT firm so we wouldlike a modern look.

Industry/Entity Type

Business

```html
<!DOCTYPE html>
<html lang="en">
<head>
<meta charset="utf-8">
<title>Novaloop Inc — Business Cards</title>
<link rel="stylesheet" href="https://fonts.googleapis.com/css2?family=Josefin+Sans:wght@400;600&family=Open+Sans:wght@400&display=swap">
<style>
  :root {
    --page-bg: #e9e7e2;
    --card-white: #ffffff;
    --brand-green: #5f7d22;
    --ink: #262626;
    --green-light: #93b33a;
    --green-dark: #5a7a25;
    --on-green: #ffffff;
    --icon-accent: #b8d46a;
  }
  * { box-sizing: border-box; margin: 0; padding: 0; }
  html, body {
    width: 1200px;
    height: 803px;
    overflow: hidden;
    background: var(--page-bg);
  }
  .canvas {
    position: relative;
    width: 1200px;
    height: 803px;
  }
  .card {
    position: absolute;
    width: 580px;
    height: 330px;
    box-shadow: 0 6px 18px rgba(0, 0, 0, 0.18);
  }
  .card-front {
    left: 60px;
    top: 80px;
    background: var(--card-white);
    display: flex;
    flex-direction: column;
    align-items: center;
    justify-content: center;
  }
  .brand-name {
    font-family: "Josefin Sans", sans-serif;
    font-weight: 600;
    font-size: 52px;
    letter-spacing: 6px;
    color: var(--brand-green);
    line-height: 1;
  }
  .slogan {
    margin-top: 14px;
    font-family: "Josefin Sans", sans-serif;
    font-weight: 400;
    font-size: 17px;
    letter-spacing: 3px;
    color: var(--ink);
    white-space: nowrap;
  }
  .card-back {
    left: 560px;
    top: 370px;
    background: linear-gradient(115deg, var(--green-light) 0%, var(--green-dark) 100%);
  }
  .contact-list {
    position: absolute;
    left: 205px;
    top: 118px;
    list-style: none;
    font-family: "Open Sans", sans-serif;
    font-size: 17px;
    color: var(--on-green);
  }
  .contact-item {
    display: flex;
    align-items: center;
    gap: 9px;
    height: 24px;
    white-space: nowrap;
  }
  .contact-icon {
    width: 16px;
    height: 16px;
    flex: none;
  }
</style>
</head>
<body>
<main class="canvas">
  <section class="card card-front" aria-label="Card front">
    <h1 class="brand-name">NOVALOOP INC</h1>
    <p class="slogan">MAKING TECHNOLOGY EFFORTLESS</p>
  </section>

  <section class="card card-back" aria-label="Card back">
    <ul class="contact-list">
      <li class="contact-item">
        <svg class="contact-icon" viewBox="0 0 16 16" aria-hidden="true">
          <rect x="4" y="1" width="8" height="14" rx="1.5" fill="var(--icon-accent)"/>
          <rect x="5.5" y="3" width="5" height="5" fill="var(--on-green)"/>
        </svg>
        <span>48-392-517</span>
      </li>
      <li class="contact-item">
        <svg class="contact-icon" viewBox="0 0 16 16" aria-hidden="true">
          <rect x="1" y="2" width="14" height="9" rx="1" fill="var(--on-green)"/>
          <rect x="2.5" y="3.5" width="11" height="6" fill="var(--icon-accent)"/>
          <rect x="6" y="11" width="4" height="2" fill="var(--on-green)"/>
          <rect x="4" y="13" width="8" height="1.5" fill="var(--on-green)"/>
        </svg>
        <span>novaloop.com</span>
      </li>
      <li class="contact-item">
        <svg class="contact-icon" viewBox="0 0 16 16" aria-hidden="true">
          <text x="8" y="13" text-anchor="middle" font-family="Open Sans, sans-serif" font-size="15" fill="var(--on-green)">@</text>
        </svg>
        <span>hello@novaloop.com</span>
      </li>
      <li class="contact-item">
        <svg class="contact-icon" viewBox="0 0 16 16" aria-hidden="true">
          <circle cx="8" cy="8" r="7" fill="var(--on-green)"/>
          <circle cx="8" cy="8" r="3" fill="var(--icon-accent)"/>
        </svg>
        <span>218 Maple Ct, Fairview, IL 60412-3307</span>
      </li>
    </ul>
  </section>
</main>
</body>
</html>
```